Tally Roster survey and prize

We need an A4 poster design for a survey and competition I wish to hold. The survey will be on Poll Parrot. My website www.TallyRoster.com.au will redirect the users to the survey page. I will be selecting a survey entrant at random to win a prize. The prize is $200 cash. The survey will be open for two months as the mail out of this poster will go throughout Victoria, Australia. The competition end date is yet to be decided - depends on when I can get this poster completed and the mail out done.

The mail out is targeting the Aged Care industry workers and decision makers. It hopefully will be placed on a notice board in the facilities and need to attract attention for people to visit my site and then take the survey.

The survey is for not for residents but for the workers in the facility.
Updates

Reason: Just got some feedback on required content of the poster. Text for the poster required: "The survey is for determining a market for rostering and payroll software, your assitance in taking this survey would be greatly appreciated." Martin Hobbs

Target Market(s)

Workers in Aged Care industry and decision makers.

Industry/Entity Type

Industry

Requirements
Must have
• 1. Must reference the website www.TallyRoster.com.au.
2. Must mention that there is a prize of $200.
3. Must mention that entry to the competition is dependant on taking the survey.
4. Must mention the close date (date yet to be decided).
5. Must mention winning contestant will be contacted by phone.

```html
<!DOCTYPE html>
<html lang="en">
<head>
<meta charset="utf-8">
<title>Tally Roster Survey Competition Poster</title>
<link rel="stylesheet" href="https://fonts.googleapis.com/css2?family=League+Gothic&family=Archivo+Black&family=Roboto:wght@400;500;700&display=swap">
<style>
  :root {
    --brand-blue: #3f5f9e;
    --ink-navy: #2b2f40;
    --panel-slate: #363945;
    --prize-yellow: #f6d13a;
    --paper: #ffffff;
    --shadow-ink: #1d2233;
  }
  * { margin: 0; padding: 0; box-sizing: border-box; }
  html, body { width: 848px; height: 1200px; overflow: hidden; background: var(--paper); }
  .poster {
    position: relative;
    width: 848px;
    height: 1200px;
    overflow: hidden;
    background: var(--paper);
    font-family: "Roboto", Arial, sans-serif;
  }
  .hero-photo {
    position: absolute;
    left: 0; top: 0;
    width: 781px; height: 1019px;
    background:
      radial-gradient(ellipse 60% 40% at 45% 80%, #22242c 0%, rgba(34,36,44,0.85) 55%, rgba(34,36,44,0) 100%),
      radial-gradient(ellipse 50% 30% at 75% 15%, #9fb6c4 0%, rgba(159,182,196,0) 100%),
      linear-gradient(180deg, #b7b53c 0%, #9aa43a 30%, #6f7d39 55%, #55573f 80%, #8a8a80 100%);
  }
  .headline {
    position: absolute;
    left: 0; top: 0;
    width: 848px; height: 720px;
  }
  .headline text {
    font-family: "League Gothic", "Oswald", sans-serif;
    paint-order: stroke;
    stroke: var(--paper);
    stroke-width: 8px;
    stroke-linejoin: round;
  }
  .headline .line-dark { fill: var(--ink-navy); }
  .headline .line-blue { fill: var(--brand-blue); }
  .headline .rule { stroke: var(--brand-blue); stroke-width: 3; }
  .survey-panel {
    position: absolute;
    left: 50px; top: 762px;
    width: 346px; height: 261px;
    border-radius: 28px;
    background: var(--panel-slate);
    color: var(--paper);
    text-align: center;
  }
  .survey-panel__lead {
    margin-top: 48px;
    font-size: 30px;
    line-height: 1.2;
    font-weight: 400;
  }
  .survey-panel__url {
    margin-top: 60px;
    font-size: 22px;
    font-weight: 500;
    color: var(--paper);
  }
  .prize-badge {
    position: absolute;
    left: 470px; top: 724px;
    width: 400px; height: 400px;
  }
  .prize-badge text { font-family: "Archivo Black", "Arial Black", sans-serif; }
  .closing-info {
    position: absolute;
    left: 58px; top: 1068px;
    color: #111;
  }
  .closing-info__date {
    font-size: 31px;
    font-weight: 500;
  }
  .closing-info__date span { font-weight: 400; }
  .closing-info__note {
    margin-top: 6px;
    font-size: 17px;
    font-weight: 400;
  }
  .footer-band {
    position: absolute;
    left: 0; bottom: 0;
    width: 848px; height: 34px;
    background: var(--brand-blue);
  }
</style>
</head>
<body>
<main class="poster">
  <div class="hero-photo" role="img" aria-label="Photo of two smiling business people in suits giving a thumbs up outdoors in a leafy park"></div>

  <svg class="headline" viewBox="0 0 848 720" aria-label="Take the survey, enter the competition, become the winner">
    <text class="line-dark" x="591" y="192" font-size="124" textLength="235" lengthAdjust="spacingAndGlyphs">TAKE THE</text>
    <text class="line-blue" x="591" y="306" font-size="142" textLength="235" lengthAdjust="spacingAndGlyphs">SURVEY</text>
    <text class="line-dark" x="591" y="406" font-size="116" textLength="235" lengthAdjust="spacingAndGlyphs">ENTER THE</text>
    <text class="line-blue" x="591" y="482" font-size="88" textLength="235" lengthAdjust="spacingAndGlyphs">COMPETETION</text>
    <text class="line-dark" x="591" y="606" font-size="152" textLength="235" lengthAdjust="spacingAndGlyphs">BECOME</text>
    <line class="rule" x1="591" y1="620" x2="826" y2="620"/>
    <text class="line-blue" x="591" y="698" font-size="95" textLength="235" lengthAdjust="spacingAndGlyphs">THE WINNER</text>
    <line class="rule" x1="591" y1="710" x2="826" y2="710"/>
  </svg>

  <section class="survey-panel">
    <p class="survey-panel__lead">Complete our<br>online survey at</p>
    <p class="survey-panel__url">www.TallyRoster.com.au</p>
  </section>

  <svg class="prize-badge" viewBox="0 0 400 400" aria-label="Win $200 cash">
    <defs>
      <clipPath id="badge-circle"><circle cx="200" cy="200" r="197"/></clipPath>
    </defs>
    <circle cx="200" cy="200" r="197" fill="var(--brand-blue)"/>
    <polygon points="0,370 400,264 400,400 0,400" fill="var(--prize-yellow)" clip-path="url(#badge-circle)"/>
    <g transform="rotate(-16 200 200)">
      <text x="182" y="148" font-size="84" text-anchor="middle" fill="var(--shadow-ink)" opacity="0.6">WIN</text>
      <text x="178" y="144" font-size="84" text-anchor="middle" fill="var(--paper)">WIN</text>
      <text x="198" y="250" font-size="108" text-anchor="middle" fill="var(--shadow-ink)" opacity="0.6">$200</text>
      <text x="194" y="246" font-size="108" text-anchor="middle" fill="var(--paper)">$200</text>
      <text x="232" y="340" font-size="40" text-anchor="middle" fill="var(--panel-slate)">CASH</text>
    </g>
  </svg>

  <section class="closing-info">
    <p class="closing-info__date">Closing Date <span>xx-xx-xxxx</span></p>
    <p class="closing-info__note">Winning Contestant will be Informed by Phone</p>
  </section>

  <div class="footer-band"></div>
</main>
</body>
</html>
```